Great Opportunity !! Masters in Business Analytics College Course

the size is Full Page, with bleed*
8”x 10.75" plus 0.25" bleed.
please leave one inch for footer
the purpose is attract students to join this college program .
this is for students in USA .
college age of around 24 years old
I am looking for a flyer that is unique and shows creativity .
A flyer that people would want to look at it because it is unique.
you can choose either vector, text ,or picture.
if you do picture it should be a white USA citizen wearing a white solid shirt and not long hair

Target Market(s)

USA students about 23 in age to join this college program

Industry/Entity Type

education

Colors
0054AA
0677BA
7BADD7
CADEEF
E8F1F8
0094D4
00A9DD
6FCCEA
C7EBF8
E9F6FB

Requirements
Must have
• the text should not be crowded .. .. .. the ad should not be full of text
Should not have
• not have very large text .. it should not be a flyer that is full of text .. you have to figure out how to avoid looking at the ad and it is very busy with text

```html
<!DOCTYPE html>
<html lang="en">
<head>
<meta charset="utf-8">
<title>Master's in Business Analytics – Open House Flyer</title>
<link rel="stylesheet" href="https://fonts.googleapis.com/css2?family=Bebas+Neue&family=Montserrat:wght@400;500;600;700&display=swap">
<style>
  :root {
    --page-bg: #e6e6e6;
    --ink-dark: #1b1b1b;
    --ink-footer: #121212;
    --panel: #222222;
    --navy: #0f2c4c;
    --white: #ffffff;
    --text-dark: #111111;
  }
  * { box-sizing: border-box; margin: 0; padding: 0; }
  html, body { width: 1200px; height: 2479px; overflow: hidden; background: var(--page-bg); }
  .canvas { position: relative; width: 1200px; height: 2479px; }
  .flyer {
    position: absolute; left: 40px; top: 469px;
    width: 959px; height: 1319px;
    transform: scale(1.168); transform-origin: 0 0;
    overflow: hidden; background: var(--ink-dark);
    font-family: "Montserrat", Arial, sans-serif; color: var(--white);
  }
  .flyer-art { position: absolute; inset: 0; }
  .display { font-family: "Bebas Neue", "Arial Narrow", sans-serif; font-weight: 400; line-height: 1; }
  .condensed { transform: scaleX(0.88); transform-origin: 0 0; }
  .headline { position: absolute; left: 70px; top: 64px; color: var(--text-dark); }
  .headline .small { font-size: 48px; display: block; }
  .headline .big { font-size: 88px; display: block; }
  .headline .gap { margin-top: 8px; }
  .intro {
    position: absolute; left: 72px; top: 446px; width: 420px;
    font-size: 19px; line-height: 24px; font-weight: 500; white-space: nowrap;
  }
  .jobs-title { position: absolute; left: 64px; top: 552px; font-size: 64px; line-height: 62px; }
  .jobs-box {
    position: absolute; left: 68px; top: 676px; width: 374px; height: 222px;
    border: 4px solid var(--white); border-top: none; border-radius: 0 0 18px 18px;
    background: var(--panel);
  }
  .jobs-source {
    background: var(--white); color: var(--text-dark);
    font-size: 30px; padding: 5px 8px 0; height: 40px; white-space: nowrap;
  }
  .jobs-list { list-style: none; padding: 6px 0 0 12px; }
  .jobs-list li { display: flex; align-items: center; gap: 10px; font-size: 21px; line-height: 25.6px; }
  .jobs-list svg { width: 18px; height: 18px; flex: none; }
  .hired { position: absolute; left: 74px; top: 936px; }
  .hired h3 { font-size: 34px; }
  .hired p { font-size: 24px; line-height: 33px; }
  .open-house { position: absolute; left: 75px; top: 1068px; }
  .open-house h2 { font-size: 40px; font-weight: 700; line-height: 44px; }
  .open-house p { font-size: 19px; line-height: 24px; }
  .college { position: absolute; left: 553px; top: 938px; }
  .college h2 { font-size: 30px; font-weight: 700; line-height: 36px; }
  .college p { font-size: 17px; line-height: 23px; }
  .duration { position: absolute; left: 552px; top: 1088px; display: flex; align-items: flex-end; }
  .duration .num { font-size: 80px; font-weight: 700; line-height: 64px; letter-spacing: -3px; }
  .duration .detail { margin-left: 6px; padding-bottom: 2px; }
  .duration .unit { font-size: 29px; font-weight: 700; line-height: 26px; display: block; }
  .duration .note { font-size: 15px; line-height: 18px; display: block; }
</style>
</head>
<body>
<div class="canvas">
  <section class="flyer">
    <svg class="flyer-art" viewBox="0 0 959 1319" width="959" height="1319">
      <defs>
        <linearGradient id="officeTone" x1="0" y1="0" x2="1" y2="1">
          <stop offset="0" stop-color="#dfe4ea"/>
          <stop offset="0.5" stop-color="#f4f6f8"/>
          <stop offset="1" stop-color="#ffffff"/>
        </linearGradient>
        <linearGradient id="photoTone" x1="0" y1="0" x2="0" y2="1">
          <stop offset="0" stop-color="#e4e7eb"/>
          <stop offset="0.35" stop-color="#9a9ea4"/>
          <stop offset="0.7" stop-color="#3a3c3f"/>
          <stop offset="1" stop-color="#262626"/>
        </linearGradient>
        <linearGradient id="swoosh" x1="0" y1="0" x2="1" y2="0">
          <stop offset="0" stop-color="#9a9a9a"/>
          <stop offset="0.5" stop-color="#ffffff"/>
          <stop offset="1" stop-color="#d8d8d8"/>
        </linearGradient>
      </defs>
      <rect class="footer-band" x="0" y="1185" width="959" height="134" fill="var(--ink-footer)"/>
      <rect role="img" aria-label="Blurred bright office background" x="0" y="0" width="959" height="527" fill="url(#officeTone)"/>
      <path d="M470,527 L959,527 L959,720 C820,800 640,858 470,866 Z" fill="#f2f4f6"/>
      <path role="img" aria-label="Photo of a smiling young professional in a dark suit, white shirt and tie" d="M505,40 L959,40 L959,712 C820,792 660,848 505,858 Z" fill="url(#photoTone)"/>
      <path d="M430,866 C640,852 820,792 959,702 L959,734 C820,812 640,862 430,866 Z" fill="url(#swoosh)"/>
      <rect x="0" y="434" width="490" height="3" fill="#ffffff"/>
      <rect class="intro-band" x="0" y="437" width="490" height="90" fill="var(--navy)"/>
    </svg>

    <h1 class="headline display condensed">
      <span class="small">Do you have an</span>
      <span class="big">Analytical Mind</span>
      <span class="small gap">And are seeking a</span>
      <span class="big gap">Profitable</span>
      <span class="big">Career?</span>
    </h1>

    <p class="intro">A Master's in Business Analytics from<br>Harlow State College can prepare you<br>for some of the most in-demand jobs.</p>

    <h2 class="jobs-title display condensed">Jobs with a median<br>salary of $100K+</h2>
    <div class="jobs-box">
      <div class="jobs-source display"><span class="condensed" style="display:inline-block">(National Labor Data Office 2023)</span></div>
      <ul class="jobs-list">
        <li><svg viewBox="0 0 20 20"><circle cx="10" cy="10" r="8" fill="none" stroke="#fff" stroke-width="1.8"/><path d="M6 10.5l3 3 6-7" fill="none" stroke="#fff" stroke-width="2"/></svg>BI Developer</li>
        <li><svg viewBox="0 0 20 20"><circle cx="10" cy="10" r="8" fill="none" stroke="#fff" stroke-width="1.8"/><path d="M6 10.5l3 3 6-7" fill="none" stroke="#fff" stroke-width="2"/></svg>Data Analyst</li>
        <li><svg viewBox="0 0 20 20"><circle cx="10" cy="10" r="8" fill="none" stroke="#fff" stroke-width="1.8"/><path d="M6 10.5l3 3 6-7" fill="none" stroke="#fff" stroke-width="2"/></svg>Data Scientist</li>
        <li><svg viewBox="0 0 20 20"><circle cx="10" cy="10" r="8" fill="none" stroke="#fff" stroke-width="1.8"/><path d="M6 10.5l3 3 6-7" fill="none" stroke="#fff" stroke-width="2"/></svg>Data Developer</li>
        <li><svg viewBox="0 0 20 20"><circle cx="10" cy="10" r="8" fill="none" stroke="#fff" stroke-width="1.8"/><path d="M6 10.5l3 3 6-7" fill="none" stroke="#fff" stroke-width="2"/></svg>Computer Systems Analyst</li>
        <li><svg viewBox="0 0 20 20"><circle cx="10" cy="10" r="8" fill="none" stroke="#fff" stroke-width="1.8"/><path d="M6 10.5l3 3 6-7" fill="none" stroke="#fff" stroke-width="2"/></svg>Financial Analyst</li>
      </ul>
    </div>

    <div class="hired">
      <h3 class="display condensed">Graduates were hired at:</h3>
      <p>Vantrel&nbsp; | Brightmoor</p>
      <p>Calderon | Norvik | Ashgrove</p>
    </div>

    <div class="open-house">
      <h2>Open House</h2>
      <p>Wednesday, April 20, 7:30 pm.</p>
      <p>Email: info@harlow.edu for the link!</p>
    </div>

    <div class="college">
      <h2>Harlow State College</h2>
      <p>Only 5% of universities<br>achieve prestigious ACBE</p>
    </div>

    <div class="duration">
      <span class="num">21</span>
      <span class="detail">
        <span class="unit">months</span>
        <span class="note">Hybrid with one weekly</span>
        <span class="note">in-person evening meeting</span>
      </span>
    </div>
  </section>
</div>
</body>
</html>
```